2367 Halvorsen Avenue Medical Centre

We are looking for a design for new medical clinic.
We are accepting new patients at this new medical centre grand opening. Walk-ins are welcome.
Our cardiac and vascular surgical specialists are department heads at St Alder's Hospital, a leading teaching hospital in Toronto. These specialists will see cardiovascular consults are well as pre-surgical and post-surgical consultations and follow-ups.
Our lab is affiliated with several nuclear medicine clinics in the GTA.
Our Services Includes:
Family Practice
Cardiology Diagnostics
Cardiac & Vascular Surgical Consultation
Ultrasound & Vascular Testing
Open 6 days a week.
Ample Free Parking
Friendly Staffs

Target Market(s)

New Patients. Families of any age. Ethnic groups including Asians & Africans.

Industry/Entity Type

Medical

Font styles to use
Serif
Sans Serif
Decorative
Script
Other font styles liked:
• Arial calibri, verdana

Requirements
Must have
• Address:
• 2367 Halvorsen Avenue East
• Unit 225
• Scarborough, Ontario
• K7T 2P4
• Tel: (416) 555-0148
Nice to have
• Caring and inviting environment.
• Simple but classy.
• Standout colors.
Should not have
• Busy images. Aside from this, any ideas are welcome.

```html
<!DOCTYPE html>
<html lang="en">
<head>
<meta charset="utf-8">
<title>Grand Opening – New Medical Clinic</title>
<link rel="stylesheet" href="https://fonts.googleapis.com/css2?family=Great+Vibes&family=Montserrat:wght@700&family=Cabin:wght@400;600&family=Open+Sans:wght@600;700&family=Roboto+Condensed:wght@700&family=Courgette&family=Oswald:wght@700&display=swap">
<style>
  :root {
    --sky: #2f98dc;
    --lime: #a8cf2f;
    --magenta: #e6226b;
    --berry: #c0176b;
    --sun: #fff200;
    --navy: #22348a;
    --teal: #1fb3d1;
    --ink: #1c1c1c;
    --white: #ffffff;
    --leaf: #84c13d;
    --rule: #d7d3cd;
  }
  * { margin: 0; padding: 0; box-sizing: border-box; }
  html, body { width: 975px; height: 1200px; overflow: hidden; background: var(--white); }
  .flyer { position: relative; width: 975px; height: 1200px; overflow: hidden; background: #fbfaf8; font-family: "Cabin", Arial, sans-serif; }
  .bands { position: absolute; inset: 0; }
  .photo-nurse {
    position: absolute; left: 617px; top: 520px; width: 358px; height: 585px;
    background: linear-gradient(180deg, #f4ede9 0%, #eedfd6 40%, #8fd0e0 72%, #5dbfd8 100%);
  }
  .photo-clipboard {
    position: absolute; left: 400px; top: 1010px; width: 217px; height: 95px;
    background: linear-gradient(180deg, #ece9f2 0%, #e4dfec 100%);
  }
  .headline {
    position: absolute; left: 72px; top: 40px;
    font-family: "Great Vibes", cursive; font-weight: 400; font-size: 158px; line-height: 1;
    color: var(--sun); white-space: nowrap; text-shadow: 0 2px 4px rgba(0,0,0,.15);
  }
  .clinic-title {
    position: absolute; left: 78px; top: 228px;
    font-family: "Montserrat", Arial, sans-serif; font-weight: 700; font-size: 61px;
    color: var(--white); letter-spacing: -1px; text-shadow: 0 3px 5px rgba(0,0,0,.35);
  }
  .address {
    position: absolute; left: 78px; top: 320px;
    font-size: 33px; line-height: 48px; color: var(--white);
  }
  .lab-badge {
    position: absolute; left: 708px; top: 300px; width: 206px; height: 200px; border-radius: 50%;
    background: radial-gradient(circle at 40% 35%, #ffffff 55%, #e3e5ea 100%);
    box-shadow: 0 4px 10px rgba(0,0,0,.3);
    display: flex; align-items: center; justify-content: center; text-align: center;
    font-family: "Open Sans", Arial, sans-serif; font-weight: 600; font-size: 21px; line-height: 28px; color: var(--navy);
  }
  .walkin-badge {
    position: absolute; left: 375px; top: 447px; width: 244px; height: 240px; border-radius: 50%;
    background: radial-gradient(circle at 45% 30%, #f6588f 0%, var(--magenta) 60%, #d31a5d 100%);
    border: 5px solid var(--white); box-shadow: 0 3px 8px rgba(0,0,0,.3);
    display: flex; align-items: center; justify-content: center; text-align: center;
    font-family: "Roboto Condensed", Arial, sans-serif; font-weight: 700; font-size: 44px; line-height: 51px;
    color: var(--white); text-shadow: 0 2px 3px rgba(0,0,0,.35);
  }
  .welcome {
    position: absolute; left: 50px; top: 592px;
    font-family: "Courgette", cursive; font-weight: 400; font-size: 44px; line-height: 52px; color: var(--leaf);
  }
  .about {
    position: absolute; left: 43px; top: 716px; width: 262px; padding-right: 36px;
    border-right: 2px solid var(--rule);
    font-size: 16.5px; line-height: 29.5px; color: var(--ink);
  }
  .services-title {
    position: absolute; left: 352px; top: 706px; width: 308px; height: 37px; border-radius: 8px;
    background: var(--teal); color: var(--white);
    font-family: "Open Sans", Arial, sans-serif; font-weight: 700; font-size: 24px; line-height: 37px; padding-left: 12px;
  }
  .services {
    position: absolute; left: 373px; top: 753px; width: 300px; list-style: none;
    font-size: 21px; line-height: 25px; color: var(--ink);
  }
  .services li { position: relative; padding-left: 22px; margin-bottom: 7px; }
  .services li::before {
    content: ""; position: absolute; left: 0; top: 6px; width: 13px; height: 13px; border-radius: 50%;
    background: var(--magenta);
  }
  .cta {
    position: absolute; left: 95px; top: 1022px; width: 300px; height: 120px;
    transform: rotate(-7deg);
  }
  .cta-text {
    position: absolute; left: 0; top: 26px; width: 300px; text-align: center;
    font-family: "Oswald", Arial, sans-serif; font-weight: 700; font-size: 33px; line-height: 34px; color: var(--ink);
  }
  .phone {
    position: absolute; right: 42px; top: 1080px; text-align: right; color: var(--white);
  }
  .phone-label { font-family: "Great Vibes", cursive; font-size: 48px; line-height: 46px; display: block; }
  .phone-number { font-family: "Roboto Condensed", Arial, sans-serif; font-weight: 700; font-size: 50px; line-height: 58px; text-shadow: 0 2px 3px rgba(0,0,0,.3); }
</style>
</head>
<body>
<main class="flyer">
  <div class="photo-nurse" role="img" aria-label="Photo of a smiling nurse in teal scrubs with a stethoscope"></div>
  <div class="photo-clipboard" role="img" aria-label="Photo of a hand writing on a clipboard"></div>

  <svg class="bands" width="975" height="1200" viewBox="0 0 975 1200" aria-hidden="true">
    <defs>
      <linearGradient id="sky" x1="0" y1="0" x2="1" y2="1">
        <stop offset="0" stop-color="#3a9fe0"/>
        <stop offset="1" stop-color="#2b8fd6"/>
      </linearGradient>
    </defs>
    <path d="M0 0 H975 V150 C880 215 770 495 575 560 C440 605 300 430 0 438 Z" fill="url(#sky)"/>
    <path d="M0 438 C300 430 440 605 575 560 C770 495 880 215 975 150 V192 C900 265 800 545 605 610 C455 660 300 505 0 500 Z" fill="var(--lime)"/>
    <path d="M0 515 C260 505 430 650 580 640 C770 628 890 330 975 205" fill="none" stroke="var(--magenta)" stroke-width="5"/>
    <path d="M0 1112 C200 1092 450 1098 640 1125 V1200 H0 Z" fill="var(--sky)"/>
    <path d="M0 1200 C260 1138 620 1108 975 1000 V1200 Z" fill="var(--lime)"/>
    <path d="M210 1200 C460 1148 720 1115 975 1020 V1200 Z" fill="var(--berry)"/>
  </svg>

  <h1 class="headline">Grand Opening</h1>
  <h2 class="clinic-title">NEW MEDICAL CLINIC</h2>
  <p class="address">2367 Halvorsen Avenue East, Unit 225,<br>Scarborough, Ontario, K7T 2P4</p>

  <div class="lab-badge">Our lab is<br>affiliated with<br>several nuclear<br>medicine clinics<br>in the GTA.</div>
  <div class="walkin-badge">Accepting<br>Walk-in<br>Patients</div>

  <h3 class="welcome">Walk-ins are<br>Welcome</h3>
  <p class="about">Our cardiac and vascular surgical specialists are department heads at St Alder's Hospital, a leading teaching hospital in Toronto. These specialists will see cardiovascular consults are well as pre-surgical and post-surgical consultations and follow-ups.</p>

  <h3 class="services-title">Our Services Includes:</h3>
  <ul class="services">
    <li>Family Practice</li>
    <li>Cardiology Diagnostics</li>
    <li>Cardiac &amp; Vascular Surgical Consultation</li>
    <li>Ultrasound &amp; Vascular Testing</li>
    <li>Open 6 days a week.</li>
    <li>Ample Free Parking</li>
    <li>Friendly Staffs</li>
  </ul>

  <div class="cta">
    <svg width="300" height="120" viewBox="0 0 300 120" aria-hidden="true">
      <path d="M30 20 C90 2 230 0 280 18 C300 40 298 90 270 108 C200 122 80 120 28 104 C6 84 8 38 30 20 Z" fill="var(--sun)"/>
      <path d="M24 16 C96 -4 236 -2 286 20 C304 46 300 96 264 114 C190 126 74 124 22 108 C0 86 2 34 24 16 Z" fill="none" stroke="#e8d900" stroke-width="2"/>
    </svg>
    <p class="cta-text">CALL FOR BOOK<br>APPOINTMENT</p>
  </div>

  <p class="phone"><span class="phone-label">Call</span><span class="phone-number">(416) 555-0148</span></p>
</main>
</body>
</html>
```